Consulting firm looking for brochure design

Loring & Vance Consulting is a firm based in Harlow Springs looking to update brochure design. We offer a broad range of development expertise to public, private and institutional clients. We would like to see brochure ideas including our company work, the services included, our individual qualifications and a list showing the clients we have served both public and private. We would like brochure to include the colors red, black, gray, and/or white only and to have our logo displayed on brochure pages. Files attached include a PPT with company information we'd like to see included in brochure, company logo designs to choose from to include in brochure, and the previous brochure that we are wanting to replace.
**Note that we are rebranding from " Warren Hollis Economic Development, LLC" to "Loring & Vance Consulting"**
**We have added a total of four logo designs; Two Portrait and Two Landscape both with the options of black backgrounds vs white backgrounds to choose from**

```html
<!DOCTYPE html>
<html lang="en">
<head>
<meta charset="utf-8">
<title>Loring &amp; Vance Consulting — Brochure</title>
<link rel="stylesheet" href="https://fonts.googleapis.com/css2?family=Lato:wght@300;400;700&family=Montserrat:wght@600;700&family=Oswald:wght@500;600&display=swap">
<style>
  :root{
    --red:#e8452c;
    --black:#1d1d1d;
    --charcoal:#3b3b3b;
    --mid-gray:#5c5c5c;
    --light-gray:#ebebeb;
    --stripe-gray:#bdbdbd;
    --text-gray:#555555;
    --white:#ffffff;
    --backdrop:#d6d6d6;
  }
  *{box-sizing:border-box;margin:0;padding:0}
  html,body{width:1063px;height:1200px;overflow:hidden}
  body{background:var(--backdrop);position:relative;font-family:"Lato",sans-serif;color:var(--text-gray)}

  .page{position:absolute;width:426px;height:552px;overflow:hidden;background:var(--white)}
  .page--cover{left:78px;top:32px}
  .page--david{left:577px;top:32px;background:var(--light-gray)}
  .page--natalie{left:78px;top:636px;background:var(--light-gray)}
  .page--clients{left:577px;top:636px;background:var(--light-gray)}
  .page-art{position:absolute;left:0;top:0;width:426px;height:552px}
  .abs{position:absolute}

  .brand{position:absolute;display:flex;align-items:center;gap:8px;font-family:"Montserrat",sans-serif;font-weight:600;text-transform:uppercase;letter-spacing:.5px}
  .brand__square{width:30px;height:30px;background:var(--red);flex:none}
  .brand--header{left:18px;top:24px;font-size:13px;color:var(--black)}
  .brand--footer{left:22px;bottom:14px;font-size:8px;color:var(--white);background:var(--black);padding:6px 8px}
  .brand--footer .brand__square{width:18px;height:18px}

  .intro{left:16px;top:140px;width:396px;font-size:10.6px;line-height:12.6px;color:var(--white);text-align:justify}
  .services-banner{left:40px;top:250px;width:346px;height:24px;font-family:"Oswald",sans-serif;font-weight:600;font-size:15px;color:var(--white);text-align:center;line-height:24px;letter-spacing:.4px}
  .services{left:6px;top:286px;width:414px;display:flex;justify-content:space-between}
  .service{width:70px;text-align:center}
  .service svg{width:28px;height:28px;display:block;margin:0 auto 6px}
  .service__label{font-size:7.2px;line-height:8.4px;color:var(--red)}
  .financial{left:22px;top:436px}
  .financial__title{font-family:"Montserrat",sans-serif;font-weight:700;font-size:18px;color:var(--red);line-height:22px}
  .financial__sub{font-family:"Lato",sans-serif;font-weight:300;font-size:20px;color:var(--white);line-height:22px;letter-spacing:.5px}
  .financial-list{left:22px;top:492px;width:390px;display:grid;grid-template-columns:200px 190px;row-gap:6px;list-style:none}
  .financial-list li{font-size:9px;color:var(--white);padding-left:14px;position:relative}

  .chev::before{content:"";position:absolute;left:2px;top:50%;width:4px;height:4px;border-right:1.6px solid var(--red);border-bottom:1.6px solid var(--red);transform:translateY(-60%) rotate(-45deg)}

  .qual-title{right:22px;top:30px;font-family:"Montserrat",sans-serif;font-weight:700;font-size:26px;color:var(--white);letter-spacing:.3px}
  .person-name{left:21px;top:128px;font-family:"Montserrat",sans-serif;font-weight:700;font-size:15px;color:var(--red)}
  .bio{left:21px;width:386px;font-size:10.9px;line-height:13.6px;color:var(--text-gray);text-align:justify}
  .page--david .bio--one{top:162px}
  .page--david .bio--two{top:280px}
  .page--natalie .bio--one{top:158px}
  .page--natalie .bio--two{top:284px}
  .education{left:21px;width:390px;font-size:10.6px;line-height:12.8px;color:var(--black)}
  .page--david .education{top:386px}
  .page--natalie .education{top:378px}
  .education__label{font-family:"Montserrat",sans-serif;font-weight:600;font-size:10px;color:var(--red);margin-bottom:2px}
  .education__degree{color:var(--red);font-weight:700}

  .tab{left:0;height:27px;padding:0 26px 0 22px;font-family:"Oswald",sans-serif;font-weight:600;font-size:15px;line-height:27px;color:var(--white);letter-spacing:.3px}
  .tab--public{top:12px;width:168px}
  .tab--private{top:254px;width:170px}
  .client-list{list-style:none;font-size:10.4px;line-height:13.5px}
  .client-list li{position:relative;padding-left:12px}
  .client-list--public{color:var(--white)}
  .client-list--private{color:var(--charcoal)}
  .public-a{left:20px;top:46px}
  .public-b{left:172px;top:46px}
  .private-a{left:22px;top:297px}
  .private-b{left:222px;top:297px}
</style>
</head>
<body>

<section class="page page--cover">
  <svg class="page-art" viewBox="0 0 426 552" aria-hidden="true">
    <polygon points="0,142 426,52 426,240 0,240" fill="var(--red)"/>
    <polygon points="0,128 426,38 426,52 0,142" fill="var(--black)"/>
    <polygon points="40,247 386,247 372,275 54,275" fill="var(--mid-gray)"/>
    <polygon points="0,380 40,360 426,428 426,434 40,366 0,386" fill="var(--stripe-gray)"/>
    <polygon points="0,392 40,372 426,440 426,552 0,552" fill="var(--black)"/>
  </svg>
  <div class="abs" role="img" aria-label="Grayscale photograph of a city skyline" style="left:0;top:352px;width:426px;height:80px;background:linear-gradient(180deg,#ffffff 0%,#d9d9d9 60%,#bfbfbf 100%);clip-path:polygon(0 36%,10% 10%,100% 0,100% 95%,10% 18%,0 40%)"></div>

  <div class="brand brand--header"><span class="brand__square"></span>Loring &amp; Vance Consulting</div>

  <p class="abs intro">Loring &amp; Vance Consulting offers a broad range of economic development and real estate development expertise to public, private, and institutional clients. With strategic guidance, we help navigate public-private partnerships, local government policies, creative incentive financing, project/program management, and many more of the challenges facing our clients. We make challenging real estate projects financially feasible by providing sensible solutions that are customized to meet the shifting needs of today’s economy.</p>

  <div class="abs services-banner">ECONOMIC DEVELOPMENT SERVICES INCLUDE:</div>

  <div class="abs services">
    <div class="service">
      <svg viewBox="0 0 30 30"><circle cx="15" cy="15" r="14" fill="var(--black)"/><path d="M7 16l5-4 3 2 3-2 5 4-5 4-3-2-3 2z" fill="var(--white)"/></svg>
      <p class="service__label">Public Private Partnership Structuring</p>
    </div>
    <div class="service">
      <svg viewBox="0 0 30 30"><circle cx="8" cy="8" r="4" fill="var(--black)"/><circle cx="22" cy="8" r="4" fill="var(--black)"/><path d="M2 22a6 6 0 0 1 12 0zM16 22a6 6 0 0 1 12 0z" fill="var(--black)"/><rect x="4" y="23" width="22" height="3" fill="var(--black)"/></svg>
      <p class="service__label">Incentive Negotiations</p>
    </div>
    <div class="service">
      <svg viewBox="0 0 30 30"><rect x="4" y="18" width="5" height="10" fill="var(--black)"/><rect x="11" y="13" width="5" height="15" fill="var(--black)"/><rect x="18" y="8" width="5" height="20" fill="var(--black)"/><path d="M20 2l5 5h-3v2h-4V7h-3z" fill="var(--black)"/></svg>
      <p class="service__label">Creating and Amending Tax Increment Reinvestments Zones</p>
    </div>
    <div class="service">
      <svg viewBox="0 0 30 30"><rect x="8" y="1" width="14" height="9" rx="2" fill="var(--black)"/><circle cx="6" cy="18" r="3" fill="var(--black)"/><circle cx="24" cy="18" r="3" fill="var(--black)"/><path d="M1 28a5 5 0 0 1 10 0zM19 28a5 5 0 0 1 10 0z" fill="var(--black)"/><circle cx="15" cy="16" r="2.5" fill="var(--black)"/></svg>
      <p class="service__label">Chapter 380 Grant Contract Negotiations</p>
    </div>
    <div class="service">
      <svg viewBox="0 0 30 30"><path d="M15 2l13 7H2z" fill="var(--black)"/><rect x="5" y="11" width="3" height="13" fill="var(--black)"/><rect x="11" y="11" width="3" height="13" fill="var(--black)"/><rect x="17" y="11" width="3" height="13" fill="var(--black)"/><rect x="23" y="11" width="3" height="13" fill="var(--black)"/><rect x="2" y="25" width="26" height="3" fill="var(--black)"/></svg>
      <p class="service__label">City Council Workshops</p>
    </div>
    <div class="service">
      <svg viewBox="0 0 30 30"><path d="M15 2l13 11h-4v14H6V13H2z" fill="var(--black)"/><circle cx="15" cy="18" r="5" fill="var(--white)"/><rect x="14" y="14.5" width="2" height="7" fill="var(--black)"/></svg>
      <p class="service__label">Economic Impact Reporting</p>
    </div>
  </div>

  <div class="abs financial">
    <p class="financial__title">FINANCIAL ANALYSIS</p>
    <p class="financial__sub">INCLUDING:</p>
  </div>
  <ul class="abs financial-list">
    <li class="chev">Taxable Value Analysis</li>
    <li class="chev">Market/Financial Feasibility</li>
    <li class="chev">Pro-forma Analysis</li>
    <li class="chev">Cost/Benefit Analysis</li>
    <li class="chev">Underwriting of Incentive Package</li>
    <li class="chev">Appraisal review</li>
  </ul>
</section>

<section class="page page--david">
  <svg class="page-art" viewBox="0 0 426 552" aria-hidden="true">
    <polygon points="0,0 426,0 426,62 340,126 0,40" fill="var(--red)"/>
    <polygon points="130,72 340,126 426,62 426,76 342,138 130,82" fill="var(--charcoal)"/>
    <polygon points="0,462 90,440 426,520 426,526 90,446 0,468" fill="var(--stripe-gray)"/>
    <polygon points="0,472 90,450 426,532 426,552 0,552" fill="var(--black)"/>
  </svg>
  <div class="abs" role="img" aria-label="Grayscale photograph of a downtown skyline" style="left:150px;top:420px;width:276px;height:100px;background:linear-gradient(180deg,rgba(190,190,190,0) 0%,#c4c4c4 70%,#b0b0b0 100%)"></div>

  <h2 class="abs qual-title">QUALIFICATIONS</h2>
  <h3 class="abs person-name">DAVID LORING</h3>
  <p class="abs bio bio--one">With over 30 years of experience, David Loring oversees economic development and real estate development projects for Loring &amp; Vance Consulting. David focuses on public-private partnerships for medium to large size real estate projects. His efforts include conducting feasibility analysis, contract negotiations and financing mechanisms such as TIF, abatements, and rebates, for both public and private sector clients. David’s extensive experience with multifaceted projects provides him with unique insight and creative solutions for complex problems.</p>
  <p class="abs bio bio--two">His previous projects include the successful development and redevelopment of The Spire, Central Commons, Granger Plaza, West Ninth Row in Harlow Springs, Texas, restructuring Triumph Park in Bellmont, Texas, Ashvale Ridge in Ashvale, Texas, and Palm Crest Mall in Port Alder, Texas. Additionally, he has both managed and created multiple tax increment reinvestment zones and public improvement districts addressing a wide range of issues throughout the state of Texas.</p>
  <div class="abs education">
    <p class="education__label">EDUCATION:</p>
    <p><span class="education__degree">Master of Public Administration</span> - University of North Plains</p>
    <p><span class="education__degree">Bachelor of Arts</span> – Political Science – Lubbock State University</p>
  </div>

  <div class="brand brand--footer"><span class="brand__square"></span>Loring &amp; Vance Consulting</div>
</section>

<section class="page page--natalie">
  <svg class="page-art" viewBox="0 0 426 552" aria-hidden="true">
    <polygon points="0,0 426,0 426,62 340,126 0,40" fill="var(--red)"/>
    <polygon points="130,72 340,126 426,62 426,76 342,138 130,82" fill="var(--charcoal)"/>
    <polygon points="0,462 90,440 426,520 426,526 90,446 0,468" fill="var(--stripe-gray)"/>
    <polygon points="0,472 90,450 426,532 426,552 0,552" fill="var(--black)"/>
  </svg>
  <div class="abs" role="img" aria-label="Grayscale photograph of a downtown skyline" style="left:150px;top:420px;width:276px;height:100px;background:linear-gradient(180deg,rgba(190,190,190,0) 0%,#c4c4c4 70%,#b0b0b0 100%)"></div>

  <h2 class="abs qual-title">QUALIFICATIONS</h2>
  <h3 class="abs person-name">NATALIE VANCE</h3>
  <p class="abs bio bio--one">Natalie focuses on economic development and real estate development projects and maximizing opportunities for public-private partnerships. Natalie is a former Business Development Coordinator for the City of Harlow Springs’ Economic Development Department. During her time with the City, her responsibilities included the implementation of incentives, including tax abatements, economic development program grants, tax increment financing, EB-5 funding, and state tax incentives.</p>
  <p class="abs bio bio--two">Prior to joining the City of Harlow Springs, Natalie was an Analyst with Meridian Valuation Group in Harlow Springs, where her work focused on commercial real estate appraisals used for loan underwriting purposes for a variety of property types, including office, hotel, industrial, retail, and multifamily. Earlier in her career, Natalie was an Associate in Keystone Realty Partners’ brokerage services division. In her role, she was responsible for negotiating and executing office and industrial lease and sale transactions.</p>
  <div class="abs education">
    <p class="education__label">EDUCATION:</p>
    <p><span class="education__degree">Master of Business Administration</span> - Corporate Finance – Trinity Ridge University</p>
    <p><span class="education__degree">BBA – Management</span> – Brazos Valley University</p>
  </div>

  <div class="brand brand--footer"><span class="brand__square"></span>Loring &amp; Vance Consulting</div>
</section>

<section class="page page--clients">
  <svg class="page-art" viewBox="0 0 426 552" aria-hidden="true">
    <polygon points="0,0 426,0 426,236 0,176" fill="var(--red)"/>
    <polygon points="180,206 426,242 426,252 180,216" fill="var(--charcoal)"/>
    <polygon points="0,12 168,12 154,39 0,39" fill="var(--charcoal)"/>
    <polygon points="0,254 170,254 156,281 0,281" fill="var(--charcoal)"/>
    <polygon points="0,462 90,440 426,520 426,526 90,446 0,468" fill="var(--stripe-gray)"/>
    <polygon points="0,472 90,450 426,532 426,552 0,552" fill="var(--black)"/>
  </svg>
  <div class="abs" role="img" aria-label="Tinted photograph of a downtown skyline" style="left:200px;top:40px;width:226px;height:170px;background:linear-gradient(180deg,rgba(232,69,44,0) 0%,rgba(200,52,32,.55) 100%);clip-path:polygon(0 0,100% 0,100% 100%,0 82%)"></div>
  <div class="abs" role="img" aria-label="Faded photograph of a historic main street" style="left:0;top:290px;width:426px;height:170px;background:linear-gradient(180deg,rgba(220,220,220,0) 0%,#d3d3d3 55%,#c6c6c6 100%)"></div>

  <div class="abs tab tab--public">PUBLIC CLIENTS:</div>
  <ul class="abs client-list client-list--public public-a">
    <li class="chev">Ambergate</li><li class="chev">Ashvale</li><li class="chev">Alderton</li><li class="chev">Cove Landing</li><li class="chev">Corvina</li><li class="chev">Cedar Ridge Point</li><li class="chev">Cordell Springs</li><li class="chev">Cranmore</li><li class="chev">Claybourne</li><li class="chev">El Portal Vista</li>
  </ul>
  <ul class="abs client-list client-list--public public-b">
    <li class="chev">Eastlake Bend</li><li class="chev">Harlow Springs</li><li class="chev">Grapeleaf</li><li class="chev">Grand Meadow</li><li class="chev">Kellerby</li><li class="chev">Kingsbridge</li><li class="chev">Midvale Plains</li><li class="chev">Laurel Club</li><li class="chev">Stanhope</li><li class="chev">Whitford</li>
  </ul>

  <div class="abs tab tab--private">PRIVATE CLIENTS:</div>
  <ul class="abs client-list client-list--private private-a">
    <li class="chev">Prairie Communities</li><li class="chev">Ashford Homes</li><li class="chev">Meridian Frontier</li><li class="chev">Bicentury Real Estate</li><li class="chev">Willow Bend Equities</li><li class="chev">Straight Edge Diversified Developments</li><li class="chev">Halloway</li><li class="chev">Parker Strand</li><li class="chev">Kestrel Realty</li>
  </ul>
  <ul class="abs client-list client-list--private private-b">
    <li class="chev">Larkin Commercial</li><li class="chev">Regal Crest Realty</li><li class="chev">Madrid Interest</li><li class="chev">RT Developments</li><li class="chev">Northgate Properties</li><li class="chev">QRS</li><li class="chev">Hal Brennan</li><li class="chev">Tamber Outlets</li><li class="chev">Benchmark Row</li><li class="chev">Allied Commercial Development</li>
  </ul>

  <div class="brand brand--footer"><span class="brand__square"></span>Loring &amp; Vance Consulting</div>
</section>

</body>
</html>
```